Clever Burrow

Create effective banner ads for the website CleverBurrow.com. We are building a re-target ad for coffee shops and/or stay at home office workers, and we would like to order 3 separate designs with the banner sizes 300x250, 728x90, 320x50, 640x100, 300x50, and 160x600, and they all need to be under 40kb of data. We have provided 9 slogans you can use in the Banner Ad Slogans and Extra Details document. Feel free to create your own slogan, and use resources found on our website.

Industry/Entity Type

Building

```html
<!DOCTYPE html>
<html lang="en">
<head>
<meta charset="utf-8">
<title>Clever Burrow – Banner Set</title>
<link rel="stylesheet" href="https://fonts.googleapis.com/css2?family=Raleway:wght@400;500;700;800&display=swap">
<style>
  :root{
    --canvas:#c0c0c0;
    --blue:#1f4fa6;
    --blue-deep:#173f8c;
    --blue-soft:#3d67b8;
    --brown-dark:#3a2a20;
    --brown-mid:#6b4a35;
    --brown-light:#8b6a52;
    --light:#eef0f3;
    --light-2:#d9dde3;
    --ink:#111;
    --white:#fff;
  }
  *{box-sizing:border-box;margin:0;padding:0}
  html,body{width:1200px;height:1200px;overflow:hidden}
  body{background:var(--canvas);position:relative;font-family:'Raleway',sans-serif}

  .ad{position:absolute;overflow:hidden;background:var(--white)}
  .ad.bordered{outline:1px solid #9aa3b3;outline-offset:-1px}
  .art{position:absolute}
  .theme-blue .art{background:linear-gradient(120deg,var(--blue-deep),var(--blue-soft) 55%,var(--blue))}
  .theme-brown .art{background:linear-gradient(120deg,var(--brown-dark),var(--brown-light) 50%,var(--brown-mid))}
  .theme-light .art{background:linear-gradient(120deg,var(--light-2),var(--light) 50%,#e3e6ea)}

  .copy{position:absolute;text-align:center;line-height:1.05}
  .theme-blue .copy,.theme-brown .copy{color:var(--white)}
  .theme-light .copy{color:var(--ink)}
  .hl{font-weight:800;display:block}
  .theme-light .hl-accent{color:var(--blue)}
  .sub{font-weight:500;display:block}
  .lead{font-weight:500;display:block}
  .pass{font-weight:800;display:inline-flex;align-items:center;gap:6px}
  .pass.plain{font-weight:500}
  .theme-light .pass{color:var(--blue)}
  .pass::before,.pass::after{content:"";display:block;width:22px;height:1px;background:currentColor}

  .brand{position:absolute;background:var(--white)}
  .theme-light .brand{background:var(--blue)}
  .name{display:flex;align-items:center;justify-content:center;gap:5px;font-weight:500;font-size:13px;letter-spacing:.3px;color:var(--blue);white-space:nowrap}
  .name::before{content:"";width:9px;height:9px;background:currentColor;flex:none}
  .theme-light .name{color:var(--white)}
  .btn{position:absolute;display:flex;align-items:center;justify-content:center;font-weight:800;font-size:13px;background:var(--blue);color:var(--white)}
  .theme-light .btn{background:var(--white);color:var(--ink)}

  /* 728x90 */
  .lb{width:582px;height:72px}
  .lb .art{left:0;top:0;width:434px;height:72px}
  .lb .brand{right:0;top:0;width:148px;height:72px}
  .lb .name{position:absolute;left:0;right:0;top:10px;font-size:12.5px}
  .lb .btn{left:30px;top:40px;width:99px;height:26px}
  .lb .head{left:6px;top:6px;width:210px}
  .lb .head .hl{font-size:19px}
  .lb .head .sub{font-size:14px;margin-top:3px}
  .lb .offer{left:222px;top:20px;width:212px}
  .lb .offer .lead{font-size:14px;margin-bottom:2px}
  .lb .offer .pass{font-size:15px}

  /* 640x100 */
  .md{width:512px;height:80px}
  .md .art{left:0;top:0;width:376px;height:80px}
  .md .brand{right:0;top:0;width:136px;height:80px}
  .md .name{position:absolute;left:0;right:0;top:14px;font-size:11.5px;letter-spacing:0;gap:4px}
  .md .name::before{width:8px;height:8px}
  .md .btn{left:19px;top:45px;width:98px;height:26px}
  .md .head{left:2px;top:10px;width:186px}
  .md .head .hl{font-size:19px}
  .md .head .sub{font-size:14px;margin-top:4px}
  .md .offer{left:184px;top:24px;width:190px}
  .md .offer .lead{font-size:13px;margin-bottom:3px}
  .md .offer .pass{font-size:15px}

  /* 300x250 */
  .sq{width:240px;height:200px}
  .sq .art{left:0;top:0;width:240px;height:152px}
  .sq .brand{left:0;top:152px;width:240px;height:48px}
  .sq .name{position:absolute;left:8px;top:16px;font-size:12px;justify-content:flex-start}
  .sq .btn{left:134px;top:11px;width:98px;height:26px}
  .sq .head{left:0;top:16px;width:240px}
  .sq .head .hl{font-size:23px}
  .sq .head .sub{font-size:17px;margin-top:3px}
  .sq .offer{left:0;top:100px;width:240px}
  .sq .offer .lead{font-size:13px;margin-bottom:3px}
  .sq .offer .pass{font-size:15px}
  .sq.theme-light .head{top:10px}
  .sq.theme-light .head .sub{font-size:12px;font-weight:400;margin-top:5px;line-height:1.25}
  .sq.theme-light .offer{top:102px}
  .sq.theme-light .offer .lead{font-size:16px}
  .sq.theme-light .offer .pass{font-size:17px}

  /* 160x600 */
  .sk{width:128px;height:480px}
  .sk .art{left:0;top:0;width:128px;height:298px}
  .sk .brand{left:0;top:298px;width:128px;height:182px}
  .sk .head{left:0;top:62px;width:128px}
  .sk .head .hl{font-size:17px;line-height:1}
  .sk .head .sub{font-size:15px;margin-top:3px}
  .sk .offer{left:0;top:186px;width:128px}
  .sk .offer .lead{font-size:14px;line-height:1.15}
  .sk .offer .pass{font-size:14px;gap:4px}
  .sk .pass::before,.sk .pass::after{width:14px}
  .sk .seal{position:absolute;left:10px;top:14px;width:108px;height:108px;border-radius:50%;border:3px solid var(--ink);display:flex;align-items:center;justify-content:center;text-align:center;font-weight:500;font-size:11px;line-height:1.2;color:var(--blue)}
  .sk.theme-light .seal{border-color:var(--white);color:var(--white)}
  .sk .btn{left:10px;top:128px;width:108px;height:29px}
  .sk.theme-light .head{top:58px}
  .sk.theme-light .head .sub{font-size:11px;font-weight:400;line-height:1.4;margin-top:10px}
  .sk.theme-light .offer{top:206px}
  .sk.theme-light .offer .lead{font-size:14px}
</style>
</head>
<body>

<!-- 728x90 set -->
<div class="ad lb theme-blue" style="left:85px;top:208px">
  <div class="art" role="img" aria-label="Coffee shop interior photo in blue tint"></div>
  <div class="copy head"><span class="hl">Coffee Shops are<br>for Socializing</span><span class="sub">Get Real Work Done</span></div>
  <div class="copy offer"><span class="lead">Schedule a Tour and get a</span><span class="pass">Free Day Pass</span></div>
  <div class="brand"><div class="name">CLEVER BURROW</div><div class="btn">CLICK HERE</div></div>
</div>

<div class="ad lb theme-brown bordered" style="left:85px;top:296px">
  <div class="art" role="img" aria-label="Co-working space with people at desks, warm tint"></div>
  <div class="copy head"><span class="hl">Let Someone Else<br>Have That Space</span><span class="sub" style="font-size:12px">Work Where Work Gets Done</span></div>
  <div class="copy offer"><span class="lead" style="font-size:13px">Custom Built Co-working Space</span><span class="pass">Free Day Pass</span></div>
  <div class="brand"><div class="name">CLEVER BURROW</div><div class="btn">CLICK HERE</div></div>
</div>

<div class="ad lb theme-light" style="left:85px;top:384px">
  <div class="art" role="img" aria-label="Bright office with brick wall, faded"></div>
  <div class="copy head" style="top:4px"><span class="hl hl-accent" style="font-size:17px">More Work &amp;</span><span class="hl" style="font-size:17px">Fewer Distractions</span><span class="sub" style="font-size:11px;font-weight:400;margin-top:2px">Dedicated Offices, Shared<br>Co-Working, Lounges and More.</span></div>
  <div class="copy offer"><span class="lead" style="font-size:16px;font-weight:400">Get Your Tour Today</span><span class="pass" style="font-size:17px">Free Day Pass</span></div>
  <div class="brand"><div class="name">CLEVER BURROW</div><div class="btn">CLICK HERE</div></div>
</div>

<!-- 640x100 set -->
<div class="ad md theme-blue bordered" style="left:85px;top:488px">
  <div class="art" role="img" aria-label="Coffee shop interior photo in blue tint"></div>
  <div class="copy head"><span class="hl">Coffee Shops are<br>for Socializing</span><span class="sub">Get Real Work Done</span></div>
  <div class="copy offer"><span class="lead">Schedule a Tour and get a</span><span class="pass">Free Day Pass</span></div>
  <div class="brand"><div class="name">CLEVER BURROW</div><div class="btn">CLICK HERE</div></div>
</div>

<div class="ad md theme-brown bordered" style="left:85px;top:584px">
  <div class="art" role="img" aria-label="Co-working space with people at desks, warm tint"></div>
  <div class="copy head"><span class="hl">Let Someone Else<br>Have That Space</span><span class="sub" style="font-size:11px;margin-top:8px">Work Where Work Gets Done</span></div>
  <div class="copy offer"><span class="lead" style="font-size:12px">Custom Built Co-working Space</span><span class="pass">Free Day Pass</span></div>
  <div class="brand"><div class="name">CLEVER BURROW</div><div class="btn">CLICK HERE</div></div>
</div>

<div class="ad md theme-light" style="left:85px;top:680px">
  <div class="art" role="img" aria-label="Bright office with brick wall, faded"></div>
  <div class="copy head" style="top:8px"><span class="hl hl-accent" style="font-size:17px">More Work &amp;</span><span class="hl" style="font-size:17px">Fewer Distractions</span><span class="sub" style="font-size:11px;font-weight:400;margin-top:2px">Dedicated Offices, Shared<br>Co-Working, Lounges and More.</span></div>
  <div class="copy offer"><span class="lead" style="font-size:16px;font-weight:400">Get Your Tour Today</span><span class="pass" style="font-size:17px">Free Day Pass</span></div>
  <div class="brand"><div class="name">CLEVER BURROW</div><div class="btn">CLICK HERE</div></div>
</div>

<!-- 300x250 set -->
<div class="ad sq theme-blue bordered" style="left:85px;top:792px">
  <div class="art" role="img" aria-label="Coffee shop interior photo in blue tint"></div>
  <div class="copy head"><span class="hl">Coffee Shops are<br>for Socializing</span><span class="sub">Get Real Work Done</span></div>
  <div class="copy offer"><span class="lead">Schedule a Tour and get a</span><span class="pass">Free Day Pass</span></div>
  <div class="brand"><div class="name">CLEVER BURROW</div><div class="btn">CLICK HERE</div></div>
</div>

<div class="ad sq theme-brown bordered" style="left:341px;top:792px">
  <div class="art" role="img" aria-label="Co-working space with people at desks, warm tint"></div>
  <div class="copy head"><span class="hl">Let Someone Else<br>Have That Space</span><span class="sub" style="font-size:14px;margin-top:6px">Work Where Work Gets Done</span></div>
  <div class="copy offer"><span class="lead">Custom Built Co-working Space</span><span class="pass">Free Day Pass</span></div>
  <div class="brand"><div class="name">CLEVER BURROW</div><div class="btn">CLICK HERE</div></div>
</div>

<div class="ad sq theme-light" style="left:597px;top:792px">
  <div class="art" role="img" aria-label="Bright office with brick wall, faded"></div>
  <div class="copy head"><span class="hl hl-accent">More Work &amp;</span><span class="hl">Fewer Distractions</span><span class="sub">Dedicated Offices, Shared<br>Co-Working, Lounges and More.</span></div>
  <div class="copy offer"><span class="lead" style="font-weight:400">Get Your Tour Today</span><span class="pass">Free Day Pass</span></div>
  <div class="brand"><div class="name">CLEVER BURROW</div><div class="btn">CLICK HERE</div></div>
</div>

<!-- 160x600 set -->
<div class="ad sk theme-blue bordered" style="left:699px;top:208px">
  <div class="art" role="img" aria-label="Coffee shop interior photo in blue tint"></div>
  <div class="copy head"><span class="hl">Coffee Shops<br>are for<br>Socializing</span><span class="sub">Get Real<br>Work Done</span></div>
  <div class="copy offer"><span class="lead">Schedule a Tour</span><span class="pass plain">and get a</span><span class="hl" style="font-size:14px">Free Day Pass</span></div>
  <div class="brand"><div class="seal">CLEVER<br>BURROW</div><div class="btn">CLICK HERE</div></div>
</div>

<div class="ad sk theme-brown bordered" style="left:843px;top:208px">
  <div class="art" role="img" aria-label="Co-working space with people at desks, warm tint"></div>
  <div class="copy head"><span class="hl">Let Someone<br>Else Have<br>That Space</span><span class="sub" style="font-weight:400">Work Where<br>Work Gets<br>Done</span></div>
  <div class="copy offer" style="top:188px"><span class="lead" style="font-weight:400">Custom Built<br>Co-working</span><span class="pass plain" style="font-weight:400">Space</span><span class="hl" style="font-size:14px">Free Day Pass</span></div>
  <div class="brand"><div class="seal">CLEVER<br>BURROW</div><div class="btn">CLICK HERE</div></div>
</div>

<div class="ad sk theme-light" style="left:987px;top:208px">
  <div class="art" role="img" aria-label="Bright office with brick wall, faded"></div>
  <div class="copy head"><span class="hl hl-accent">More Work</span><span class="hl">&amp; Fewer</span><span class="hl hl-accent">Distractions</span><span class="sub">Dedicated Offices,<br>Shared Co-Working,<br>Lounges and More.</span></div>
  <div class="copy offer"><span class="lead" style="font-weight:400">Get Your Tour</span><span class="pass plain" style="color:var(--ink);font-weight:400">Today</span><span class="hl hl-accent" style="font-size:14px">Free Day Pass</span></div>
  <div class="brand"><div class="seal">CLEVER<br>BURROW</div><div class="btn">CLICK HERE</div></div>
</div>

</body>
</html>
```